Yard sign

I want it to look similar to this one,

change name to DRAVEK and submit new ideas

Also would like to improvise a bit. let's not make exactly the same thing

would like to change to: Connecticut #1 Company

also change phone to 203-555-0147
and website to
dravekllc.com

this is yard sign. size is 24' Width and 32' Height

Target Market(s)

Roof

Industry/Entity Type

Roofing

Requirements
Must have
• similar colors or add something new

```html
<!DOCTYPE html>
<html lang="en">
<head>
<meta charset="utf-8">
<title>Dravek Yard Sign</title>
<link rel="stylesheet" href="https://fonts.googleapis.com/css2?family=Fira+Sans+Condensed:wght@500;800;900&family=Fira+Sans+Extra+Condensed:ital,wght@0,800;0,900;1,800&display=swap">
<style>
  :root {
    --backdrop: #eceeef;
    --sign-black: #0c1612;
    --brand-green: #8cc63f;
    --brand-green-shade: #6fa832;
    --field-green-light: #7cc04b;
    --field-green-dark: #4f8f3a;
    --arrow-red: #ec1c24;
    --text-white: #ffffff;
  }
  * { margin: 0; padding: 0; box-sizing: border-box; }
  html, body {
    width: 1200px;
    height: 740px;
    overflow: hidden;
    background: var(--backdrop);
  }
  .canvas {
    position: relative;
    width: 1200px;
    height: 740px;
  }
  .yard-sign {
    position: absolute;
    left: 345px;
    top: 30px;
    width: 510px;
    height: 680px;
    background: var(--sign-black);
    overflow: hidden;
  }
  .sign-shapes {
    position: absolute;
    inset: 0;
    width: 510px;
    height: 680px;
  }
  .tagline {
    position: absolute;
    top: 62px;
    left: 0;
    width: 100%;
    text-align: center;
    white-space: nowrap;
    font-family: "Fira Sans Extra Condensed", sans-serif;
    font-weight: 800;
    font-size: 44px;
    line-height: 1;
    color: var(--text-white);
    letter-spacing: 0.5px;
  }
  .company-name {
    position: absolute;
    top: 118px;
    left: 34px;
    right: 34px;
    text-align: center;
    white-space: nowrap;
    font-family: "Fira Sans Extra Condensed", sans-serif;
    font-weight: 900;
    font-size: 136px;
    line-height: 1;
    color: var(--brand-green);
    text-shadow: 3px 3px 0 var(--brand-green-shade);
  }
  .brand-mark {
    position: absolute;
    top: 452px;
    right: 36px;
    display: flex;
    align-items: center;
    gap: 12px;
  }
  .brand-dot {
    width: 40px;
    height: 40px;
    border-radius: 50%;
    background: var(--text-white);
  }
  .brand-name {
    font-family: "Fira Sans Condensed", sans-serif;
    font-weight: 500;
    font-size: 13px;
    line-height: 1.25;
    color: var(--text-white);
    text-align: right;
    letter-spacing: 1px;
    text-transform: uppercase;
  }
  .phone {
    position: absolute;
    top: 516px;
    left: 0;
    width: 100%;
    text-align: center;
    white-space: nowrap;
    font-family: "Fira Sans Condensed", sans-serif;
    font-weight: 900;
    font-size: 78px;
    line-height: 1;
    color: var(--text-white);
    letter-spacing: 0.5px;
  }
  .web-band {
    position: absolute;
    top: 608px;
    left: 0;
    width: 100%;
    height: 49px;
    background: var(--sign-black);
    display: flex;
    align-items: center;
    justify-content: center;
  }
  .website {
    font-family: "Fira Sans Extra Condensed", sans-serif;
    font-weight: 800;
    font-style: italic;
    font-size: 34px;
    color: var(--text-white);
    letter-spacing: 0.5px;
    white-space: nowrap;
  }
</style>
</head>
<body>
  <main class="canvas">
    <section class="yard-sign" aria-label="Dravek yard sign">
      <svg class="sign-shapes" viewBox="0 0 510 680" aria-hidden="true">
        <defs>
          <linearGradient id="fieldGreen" x1="0" y1="0" x2="1" y2="0">
            <stop offset="0" stop-color="#7cc04b"/>
            <stop offset="0.55" stop-color="#4f8f3a"/>
            <stop offset="1" stop-color="#7cc04b"/>
          </linearGradient>
        </defs>
        <polygon class="green-field" points="0,457 356,362 362,390 510,261 510,680 0,680" fill="url(#fieldGreen)"/>
        <polygon class="growth-arrow" points="0,457 320,306 317,262 510,262 362,390 356,362" fill="#ec1c24"/>
        <rect class="bottom-strip" x="0" y="657" width="510" height="23" fill="url(#fieldGreen)"/>
      </svg>

      <p class="tagline">CONNECTICUT #1 COMPANY</p>
      <h1 class="company-name">DRAVEK</h1>

      <div class="brand-mark">
        <span class="brand-dot"></span>
        <p class="brand-name">Dravek<br>Restoration<br>Remodeling Group LLC</p>
      </div>

      <p class="phone">203-555-0147</p>

      <div class="web-band">
        <p class="website">WWW.DRAVEKLLC.COM</p>
      </div>
    </section>
  </main>
</body>
</html>
```